Invitation Design Project

In May 2014, my husband and I celebrate our 10th wedding anniversary, and in June 2014 I celebrate my 40th birthday. We will be having a "10/40" party in June 2014 for both events.

This party will be held on my property, "Tallowmere Farm" in North Queensland, so the invitation needs to be fun, whimsical and reflective of both our farm and the Australian bush. You can see photos of our property on facebook: https://www.plinkspace.example/tallowmerefarm

The party will be held on 7 June 2014, RSVP by 1 April 2014.

Target Market(s)

Our family and friends - all ages and backgrounds

Industry/Entity Type

Wedding

Requirements
Must have
• Must have the following details: (wording is flexible)
- Wendy & Martin celebrate their 10th wedding anniversary on 8 May 2014.
- Wendy turns 40 on 9 June 2014
- Party to be held on Tallowmere Farm, 6pm start. Dinner, entertainment and courtesy bus provided, BYO drinks.
- RSVP by 1 April 2014
Must have correct spelling and grammar on the first draft please.
Nice to have
• It might be fun if the invitation could include our pets (dogs, cats, goats, pigs, chickens, parrakeet - see pictures on the facebook link above) in some way, in cartoon form in the background maybe?
Should not have
• I'm not particularly interested in having our photos incorporated into the invitation.

```html
<!DOCTYPE html>
<html lang="en">
<head>
<meta charset="utf-8">
<title>Wendy &amp; Martin's 10/40 Party Invitation</title>
<link rel="stylesheet" href="https://fonts.googleapis.com/css2?family=Cinzel:wght@700;900&family=Dancing+Script:wght@500&family=Advent+Pro:wght@400&family=Playfair+Display:ital,wght@1,500&display=swap">
<style>
  :root {
    --gold: #f2c21a;
    --blue: #1e5c9c;
    --magenta: #e83fe0;
    --white: #f7f7f2;
    --pen-grey: #7f98a6;
    --pen-dark: #3d5664;
    --sky: #eef3ea;
    --leaf: #a9c77e;
    --pig: #23232c;
  }
  * { margin: 0; padding: 0; box-sizing: border-box; }
  html, body { width: 1200px; height: 847px; overflow: hidden; background: #ffffff; }
  .invitation {
    position: relative;
    width: 1200px;
    height: 847px;
    overflow: hidden;
  }
  .farm-scene {
    position: absolute;
    inset: 0;
    background:
      radial-gradient(ellipse 380px 260px at 880px 130px, var(--sky) 0%, rgba(238,243,234,0.85) 45%, rgba(238,243,234,0) 100%),
      radial-gradient(ellipse 260px 160px at 1000px 120px, rgba(169,199,126,0.6) 0%, rgba(169,199,126,0) 100%),
      radial-gradient(ellipse 520px 560px at 960px 560px, var(--pig) 0%, var(--pig) 55%, rgba(35,35,44,0) 100%),
      linear-gradient(100deg, var(--pen-grey) 0%, #9fb3bd 30%, var(--pen-dark) 48%, #5f7580 62%, var(--pig) 100%);
  }
  .headline {
    position: absolute;
    left: 70px;
    top: 148px;
    width: 445px;
    text-align: center;
    font-family: "Cinzel", serif;
    font-weight: 700;
    font-size: 46px;
    line-height: 69px;
    letter-spacing: 3px;
    color: var(--gold);
  }
  .ten-forty, .party {
    position: absolute;
    left: 66px;
    width: 450px;
    text-align: center;
    font-family: "Cinzel", serif;
    font-weight: 900;
    color: var(--blue);
    line-height: 1;
  }
  .ten-forty { top: 478px; font-size: 104px; letter-spacing: 2px; }
  .party { top: 632px; font-size: 104px; letter-spacing: 4px; }
  .occasion {
    position: absolute;
    font-family: "Dancing Script", cursive;
    font-size: 19px;
    line-height: 24px;
    color: var(--gold);
    text-align: center;
  }
  .occasion-anniversary { left: 62px; top: 586px; width: 150px; }
  .occasion-birthday { left: 345px; top: 590px; width: 165px; }
  .byob {
    position: absolute;
    left: 728px;
    top: 282px;
    font-family: "Playfair Display", serif;
    font-style: italic;
    font-weight: 500;
    font-size: 48px;
    letter-spacing: 4px;
    color: var(--magenta);
    transform: rotate(-28deg);
    transform-origin: left bottom;
  }
  .details {
    position: absolute;
    left: 803px;
    top: 346px;
    font-family: "Advent Pro", sans-serif;
    font-size: 44px;
    line-height: 70px;
    color: var(--white);
    list-style: none;
  }
  .provisions {
    position: absolute;
    left: 657px;
    top: 578px;
    width: 510px;
    font-family: "Advent Pro", sans-serif;
    font-size: 30px;
    letter-spacing: 0.4px;
    color: var(--white);
    white-space: nowrap;
  }
  .rsvp {
    position: absolute;
    left: 760px;
    top: 728px;
    font-family: "Playfair Display", serif;
    font-style: italic;
    font-size: 27px;
    letter-spacing: 1px;
    color: var(--gold);
    transform: rotate(-16deg);
    transform-origin: left center;
    white-space: nowrap;
  }
</style>
</head>
<body>
  <main class="invitation">
    <div class="farm-scene" role="img" aria-label="Posterised photo of a black pig poking its snout through the rails of a grey farm pen, with sky and foliage behind"></div>

    <h1 class="headline">You are cordially invited to Wendy &amp; Martin’s</h1>

    <p class="ten-forty">10 / 40</p>
    <p class="occasion occasion-anniversary">Years of Marriage<br>8 May 2014</p>
    <p class="occasion occasion-birthday">Wendy’s Birthday<br>9 June 2014</p>
    <p class="party">PARTY</p>

    <p class="byob">BYOB</p>
    <ul class="details">
      <li>Place: Tallowmere Farm</li>
      <li>Date: 7 June 2014</li>
      <li>Time: Starts at 6pm</li>
    </ul>
    <p class="provisions">Dinner, entertainment, &amp; courtesy bus provided</p>

    <p class="rsvp">RSVP by 1 April 2014</p>
  </main>
</body>
</html>
```